Professional, Attractive, Simple Website Needed!!

We completed the design for our logo.

We need a website built out around this.

Here are a couple samples of how we want ours formatted.

http://brvntapower.com

http://www.halvorbeam.com/lp/free-quote?LeadSource=Search%20Engine&ProgramName=webquery&experience=qual&language=en&type=brd&gclid=Xq7RTPwmEYKDLAvUHbsNQkfPZrTcGwnJuoVbXeLqHmRYdAsWtPkMcNfBYgzTrUoQJhEdWvKpYaLsZbCmNDgQwTxAoKpXbT_qkR

http://morvalo.co

Reason: Extending this deadline due to our delay in providing designers with content for each page. This is coming in next 24 hours.

Reason: Due to scheduling conflicts and extended travel delays related to Puerto Rico, the deadline has been extended. Your patience is greatly appreciated.

Reason: Travel and scheduling conflicts have made it impossible to give this project the thorough review it deserves, therefore I am extending the deadline. Thank you for your patience!

Target Market(s)

Home Owners who earn 60k + household annually

Industry/Entity Type

It Professional

Coding

Coded - Design and coding required

Number of Pages Required

5+ page

Font styles to use
Serif

Colors
34a7d8
9bcb3c

Requirements
Must have
• Simple
• Lead form Entry (Ability for visitor to enter Name, number and address for a quote)
• Sleek Design
• Professional
• Testimonials
• Use color Scheme of Design Logo Attached
Nice to have
• Video when site starts
• Like this
• https://www.vidmarrow.com/watch?v=qT8mRpXw2Ka&feature=vidm.ro
Should not have
• Should not include Commercial solar
• Should not include wind power

```html
<!DOCTYPE html>
<html lang="en">
<head>
<meta charset="utf-8">
<title>Lumora Home Energy</title>
<link rel="stylesheet" href="https://fonts.googleapis.com/css2?family=Tinos:wght@400;700&family=Open+Sans:ital,wght@0,400;0,600;1,400;1,600&display=swap">
<style>
:root{
  --blue:#34a7d8;
  --green:#9bcb3c;
  --white:#ffffff;
  --ink:#111214;
  --panel:#1a1b1d;
  --muted:#c9ccd0;
  --serif:"Tinos", "Times New Roman", serif;
  --sans:"Open Sans", Arial, sans-serif;
}
*{margin:0;padding:0;box-sizing:border-box}
html,body{width:1200px;height:3203px;overflow:hidden}
body{position:relative;background:var(--ink);color:var(--white);font-family:var(--sans)}
.abs{position:absolute}

/* Hero */
.hero-photo{left:0;top:0;width:1200px;height:822px;
  background:linear-gradient(180deg,#3b2a55 0%,#8a3d6a 18%,#d2546b 30%,#5b3a55 44%,#2a2c38 62%,#1c1f26 100%)}
.brand{display:flex;align-items:center;gap:12px;font-family:var(--serif);font-size:26px;color:var(--green);line-height:1.05}
.brand-mark{width:44px;height:44px;border-radius:50%;background:var(--blue);flex:none}
.hero-brand{left:47px;top:52px;width:200px}
.nav{left:606px;top:58px;display:flex;gap:0;font-family:var(--serif);font-size:14px;text-transform:uppercase}
.nav a{position:absolute;color:var(--white);text-decoration:none;white-space:nowrap}
.nav a.active{padding-bottom:6px;border-bottom:2px solid var(--green)}
.welcome{left:64px;top:196px;width:680px;height:96px}
.welcome h1{position:absolute;left:38px;top:22px;font-family:var(--serif);font-weight:400;font-size:48px;white-space:nowrap}
.hero-text{left:100px;top:328px;width:610px;font-size:18px;line-height:28px;color:#f0eef2}
.btn-outline{left:100px;top:472px;width:201px;height:68px;border:2px solid var(--white);color:var(--blue);font-size:22px;display:flex;align-items:center;justify-content:center}
.play{left:566px;top:478px}
.zip-title{left:0;top:650px;width:1200px;text-align:center;font-family:var(--serif);font-size:17px;text-transform:uppercase;letter-spacing:.3px}
.zip-input{left:367px;top:696px;width:229px;height:49px;border:2px solid #c9c9c9;background:rgba(20,22,28,.55);display:flex;align-items:center;padding-left:14px;gap:10px;font-size:17px;letter-spacing:1px}
.quote-btn{left:615px;top:696px;width:239px;height:49px;background:var(--blue);display:flex;align-items:center;justify-content:center;font-size:18px;letter-spacing:1.5px}

/* Outage */
.outage-photo{left:0;top:822px;width:1200px;height:363px;
  background:linear-gradient(90deg,#9c9a90 0%,#d9d4c8 12%,#6e6a62 25%,#3c4650 50%,#5d5a52 75%,#d4d0c6 88%,#8d8a80 100%)}
.outage-shade{left:0;top:822px;width:1200px;height:363px;background:rgba(15,18,22,.45)}
.outage h2{position:absolute;left:0;top:938px;width:1200px;text-align:center;font-family:var(--serif);font-weight:400;font-size:43px}
.outage-text{left:282px;top:1003px;width:636px;text-align:center;font-size:17px;line-height:29px}
.btn-green{left:515px;top:1112px;width:151px;height:43px;background:var(--green);font-size:17px;display:flex;align-items:center;justify-content:center}

/* Benefits */
.benefits-photo{left:0;top:1185px;width:1200px;height:613px;
  background:linear-gradient(135deg,#1c2a36 0%,#2a241e 35%,#3a2c20 60%,#1a1714 100%)}
.benefits-shade{left:0;top:1185px;width:1200px;height:613px;background:rgba(10,10,12,.45)}
.benefit-icon{width:106px;height:106px;border-radius:50%;background:var(--green);display:flex;align-items:center;justify-content:center}
.benefit h3{position:absolute;left:188px;font-family:var(--serif);font-weight:400;font-size:20px;text-transform:uppercase;white-space:nowrap}
.benefit p{position:absolute;left:188px;width:300px;font-size:14px;line-height:22px;color:#e4e4e4}
.benefit a{position:absolute;left:188px;font-family:var(--serif);font-size:11px;color:var(--white);text-decoration:none;padding-bottom:3px;border-bottom:1px solid var(--blue)}
.install-photo{left:591px;top:1302px;width:560px;height:376px;border:2px solid var(--blue);
  background:linear-gradient(170deg,#8ea2b6 0%,#c7cfd8 22%,#37414e 45%,#1f2836 70%,#4a5566 100%)}

/* Testimonials */
.testimonials{left:0;top:1798px;width:1200px;height:480px;background:var(--panel)}
.section-title{position:absolute;left:0;width:1200px;text-align:center;font-family:var(--serif);font-weight:700;font-size:28px;text-transform:uppercase}
.rule{position:absolute;height:2px;width:36px;left:582px;background:#8a8d92}
.arrow{width:24px;height:24px;border-radius:50%;background:var(--blue);display:flex;align-items:center;justify-content:center}
.card{position:absolute;top:1985px;width:316px;height:231px;border:2px solid var(--blue)}
.card p{position:absolute;left:20px;top:30px;width:272px;text-align:center;font-size:13px;line-height:23px}
.card .stars{position:absolute;left:0;top:127px;width:312px;text-align:center;color:#f3c622;font-size:12px;letter-spacing:2px}
.card .name{position:absolute;left:0;top:153px;width:312px;text-align:center;color:var(--green);font-weight:600;font-size:16px}
.card .role{position:absolute;left:0;top:180px;width:312px;text-align:center;font-size:12px}
.avatar{width:72px;height:72px;border-radius:50%;border:3px solid #e5e5e5;background:linear-gradient(160deg,#8a8f96,#4b4f55)}

/* Lead form */
.form-photo{left:0;top:2278px;width:1200px;height:594px;
  background:linear-gradient(180deg,#1d2128 0%,#3a3e48 30%,#2e3944 60%,#1e2630 82%,#6a5a4c 100%)}
.form-panel{left:254px;top:2331px;width:698px;height:466px;background:rgba(90,90,96,.38)}
.form-panel h2{position:absolute;left:0;top:20px;width:698px;text-align:center;font-family:var(--serif);font-weight:400;font-size:36px}
.form-panel .rule{left:313px;top:75px;width:72px;background:var(--blue)}
.field{position:absolute;border-bottom:1px solid #d8d8d8;font-style:italic;font-size:17px;color:var(--green);padding-bottom:4px}
.submit{position:absolute;left:265px;top:408px;width:164px;height:47px;border:2px solid var(--white);display:flex;align-items:center;justify-content:center;font-style:italic;font-weight:600;font-size:19px}

/* Footer */
.footer{left:0;top:2872px;width:1200px;height:331px;background:#050607;border-top:3px solid var(--blue)}
.foot-brand{left:51px;top:2972px;width:200px}
.foot-col{position:absolute;top:2942px}
.foot-col h4{font-family:var(--serif);font-weight:400;font-size:18px;padding-bottom:6px;border-bottom:2px solid var(--blue);display:inline-block;margin-bottom:14px}
.foot-col li{list-style:none;font-size:12px;line-height:22px;color:#dedede}
.foot-col.links li{font-family:var(--serif);text-transform:uppercase}
.social{display:flex;gap:12px;margin-top:4px}
.social span{width:24px;height:24px;background:#8f9297}
</style>
</head>
<body>

<!-- Hero -->
<div class="abs hero-photo" role="img" aria-label="Rooftop solar panels under a pink and purple sunset sky"></div>

<div class="abs brand hero-brand"><span class="brand-mark"></span><span>Lumora Home Energy</span></div>

<nav class="abs nav">
  <a class="active" href="#" style="left:0">Home</a>
  <a href="#" style="left:73px">About</a>
  <a href="#" style="left:156px">Morvalo Foundation</a>
  <a href="#" style="left:327px">Blog</a>
  <a href="#" style="left:400px">FAQ</a>
  <a href="#" style="left:462px">Contact Us</a>
</nav>

<div class="abs welcome">
  <svg width="680" height="96" viewBox="0 0 680 96"><polygon points="40,0 680,0 640,96 0,96" fill="#6f8aa8" fill-opacity=".55"/></svg>
  <h1>Welcome To Lumora Home Energy</h1>
</div>

<p class="abs hero-text">Lorem Ipsum is simply dummy text of the printing and typesetting industry. Lorem Ipsum has been the industry's standard dummy text ever since the 1500s, when an unknown printer took a galley</p>

<div class="abs btn-outline">READ MORE</div>

<svg class="abs play" width="56" height="56" viewBox="0 0 56 56">
  <circle cx="28" cy="28" r="26" fill="none" stroke="#fff" stroke-width="2.5"/>
  <polygon points="22,17 39,28 22,39" fill="none" stroke="#fff" stroke-width="2.5" stroke-linejoin="round"/>
</svg>

<p class="abs zip-title">Enter your zip code to see if solar works for you.</p>
<div class="abs zip-input">
  <svg width="14" height="20" viewBox="0 0 14 20"><path d="M7 0C3 0 0 3 0 7c0 5 7 13 7 13s7-8 7-13c0-4-3-7-7-7zm0 10a3 3 0 110-6 3 3 0 010 6z" fill="#34a7d8"/></svg>
  <span>Zip Code</span>
</div>
<div class="abs quote-btn">Get a free quote</div>

<!-- Outage -->
<section class="outage">
  <div class="abs outage-photo" role="img" aria-label="Modern home patio with glass doors, outdoor table and potted plants"></div>
  <div class="abs outage-shade"></div>
  <h2>Power through any outage</h2>
  <p class="abs outage-text">Lorem Ipsum is simply dummy text of the printing and typesetting industry. Lorem Ipsum has been the industry's standard dummy text ever since the 1500s, when an unknown printer</p>
  <div class="abs btn-green">LEARN MORE</div>
</section>

<!-- Benefits -->
<section class="benefits">
  <div class="abs benefits-photo" role="img" aria-label="Evening deck of a modern home lit by warm lights"></div>
  <div class="abs benefits-shade"></div>

  <div class="benefit">
    <div class="abs benefit-icon" style="left:49px;top:1271px">
      <svg width="44" height="44" viewBox="0 0 44 44" fill="none" stroke="#fff" stroke-width="2.5"><circle cx="22" cy="22" r="18"/><ellipse cx="22" cy="22" rx="8" ry="18"/><line x1="4" y1="22" x2="40" y2="22"/><path d="M7 13h30M7 31h30"/></svg>
    </div>
    <h3 style="top:1294px">Save Money</h3>
    <p style="top:1330px">Lorem Ipsum is simply dummy text of the print-ing and typesetting industry.</p>
    <a href="#" style="top:1388px">READ MORE</a>
  </div>

  <div class="benefit">
    <div class="abs benefit-icon" style="left:49px;top:1435px">
      <svg width="44" height="44" viewBox="0 0 44 44" fill="none" stroke="#fff" stroke-width="2.5" stroke-linejoin="round"><path d="M4 22L22 6l18 16"/><path d="M9 18v20h26V18"/><path d="M18 38V27h8v11"/></svg>
    </div>
    <h3 style="top:1455px">Increase Home Value</h3>
    <p style="top:1491px">Lorem Ipsum is simply dummy text of the print-ing and typesetting industry.</p>
    <a href="#" style="top:1549px">READ MORE</a>
  </div>

  <div class="benefit">
    <div class="abs benefit-icon" style="left:49px;top:1595px">
      <svg width="44" height="44" viewBox="0 0 44 44" fill="none" stroke="#fff" stroke-width="2.5"><circle cx="22" cy="22" r="18"/><circle cx="22" cy="22" r="8"/><path d="M9 9l7 7M35 9l-7 7M9 35l7-7M35 35l-7-7"/></svg>
    </div>
    <h3 style="top:1616px">Own Your Energy</h3>
    <p style="top:1652px">Lorem Ipsum is simply dummy text of the print-ing and typesetting industry.</p>
    <a href="#" style="top:1710px">READ MORE</a>
  </div>

  <div class="abs install-photo" role="img" aria-label="Installers fitting solar panels on a roof under a cloudy sky"></div>
</section>

<!-- Testimonials -->
<section class="abs testimonials"></section>
<h2 class="section-title" style="top:1831px">Testimonials</h2>
<div class="rule" style="top:1884px"></div>
<div class="abs arrow" style="left:1032px;top:1895px"><svg width="8" height="10" viewBox="0 0 8 10"><path d="M6 1L2 5l4 4" stroke="#fff" stroke-width="2" fill="none"/></svg></div>
<div class="abs arrow" style="left:1062px;top:1895px"><svg width="8" height="10" viewBox="0 0 8 10"><path d="M2 1l4 4-4 4" stroke="#fff" stroke-width="2" fill="none"/></svg></div>

<div class="card" style="left:85px">
  <p>Lorem ipsum dolor sit amet, consectetuer adipiscing elit. Aenean commodo ligula eget dolor. Aenean massa. Cum sociis</p>
  <div class="stars">★★★★★</div>
  <div class="name">Dean Rowley</div>
  <div class="role">Director, Environmental</div>
</div>
<div class="card" style="left:429px">
  <p>Lorem ipsum dolor sit amet, consectetuer adipiscing elit. Aenean commodo ligula eget dolor. Aenean massa. Cum sociis</p>
  <div class="stars">★★★★★</div>
  <div class="name">Sonia Garrett</div>
  <div class="role">Founder, Environmental</div>
</div>
<div class="card" style="left:771px">
  <p>Lorem ipsum dolor sit amet, consectetuer adipiscing elit. Aenean commodo ligula eget dolor. Aenean massa. Cum sociis</p>
  <div class="stars">★★★★★</div>
  <div class="name">Felipe Warner</div>
  <div class="role">CEO, Environmental</div>
</div>
<div class="abs avatar" style="left:122px;top:1935px" role="img" aria-label="Customer portrait"></div>
<div class="abs avatar" style="left:464px;top:1935px" role="img" aria-label="Customer portrait"></div>
<div class="abs avatar" style="left:805px;top:1935px" role="img" aria-label="Customer portrait"></div>

<!-- Lead form -->
<div class="abs form-photo" role="img" aria-label="Wind turbines and solar field at dusk"></div>
<form class="abs form-panel">
  <h2>Start Saving Today</h2>
  <div class="rule"></div>
  <div class="field" style="left:38px;top:124px;width:289px">Name</div>
  <div class="field" style="left:367px;top:124px;width:289px">Phone</div>
  <div class="field" style="left:38px;top:205px;width:618px">Email</div>
  <div class="field" style="left:38px;top:266px;width:618px;height:102px">Comment</div>
  <div class="submit">Submit</div>
</form>

<!-- Footer -->
<footer class="abs footer"></footer>
<div class="abs brand foot-brand"><span class="brand-mark"></span><span>Lumora Home Energy</span></div>

<div class="foot-col" style="left:391px">
  <h4>Latest News</h4>
  <ul>
    <li>Environment Perspective</li>
    <li>New Ecological Bulbs</li>
    <li>Protect the Environment</li>
    <li>Make Plants Alive</li>
  </ul>
</div>
<div class="foot-col links" style="left:634px">
  <h4>Usefull Links</h4>
  <ul>
    <li>Home</li>
    <li>About</li>
    <li>Morvalo Foundation</li>
    <li>Blog</li>
  </ul>
</div>
<div class="foot-col" style="left:905px">
  <h4>Social Links</h4>
  <div class="social"><span></span><span></span><span></span><span></span><span></span><span></span><span></span></div>
</div>

</body>
</html>
```